London Based Property Finding Company - have logo already

We find property for private purchasers and investors in London, UK.  We work for the BUYER, whereas estate agencies/real estate companies work for the seller. We offer a much more personalised service to UK and overseas purchasers.

We would like the following:

*A double sided business card

*A letterhead

We have attached two versions of the logo. Each logo style is set on two different coloured backgrounds. Please choose one of the two designs, whichever you prefer or feel more comfortable with, and produce one in black and one in white background.

This applies to both pieces of stationery.

THE BUSINESS CARD:

We would like the company name placed on its own on one side of the card and the contact details and what we do on the other.

e.g.

SIDE 1:

BRAMWELL PROPERTY FINDERS

SIDE 2:

Owen Bramwell

t: 0208 394 2261

m: +44(0)7940 318 472

e: info@bramwellpropertyfinders.co.uk

w: bramwellpropertyfinders.co.uk

London Property Finders and Search Agents

I will leave the layout up to you, but a minimalist layout is preferred. If you would like to put additional detial or design on the card then that is up to, but not specified.

It is optional to have the company name on side 2, but if you do use it, please make it smaller. than on the 1st side.

The design needs to be simple, professional and not too in your face.

If you are using the black background design on side 1 for the logo, then maybe a white backgounnd can be used on side 2 with a black typeface.

The type face for the contacts details should be sans serif standard typeface. Please experiment with the desciprtion.

-

THE LETTERHEAD;

You can experiment with the layout for the letterhead. e.g logo centre aligned on the top of the page with the contact details and address at the bottom of the page OR the logo, description running along a bar on the top of the page with the contact details and website address at the bottom. Please try and experiment with this, but the less 'busy', the better.

Here is info that needs to be on the letterhead.

Bramwell Property Finders

t: 0208 394 2261

m: +44(0)7940 318 472

(PLEASE NOTE; the below company info must be placed at the bottom of the page as a footer, in small text.)

Pemberly Holdings Ltd Trading as Bramwell Property Finders, a company registered in England & Wales, No.5917302 , Registered office is 41 Kelmscott House, Ashdown Lane, London, SW9 7QJ, t: 0208 394 2261, m: +44(0)7940 318 472, e: info@bramwellpropertyfinders.co.uk

Best of luck!

Thank you

Dear Designer,

I have now attached the supporting files to this brief.

Thanks,

Owen Bramwell
Bramwell Property Finders

```html
<!DOCTYPE html>
<html lang="en">
<head>
<meta charset="utf-8">
<title>Bramwell Property Finders – Stationery</title>
<link rel="stylesheet" href="https://fonts.googleapis.com/css2?family=Ubuntu:wght@400;500&display=swap">
<style>
:root{
  --ink-black:#000;
  --paper:#fff;
  --navy:#1f2f5c;
  --maroon:#7a0f24;
  --sky:#6ec6f0;
  --edge:#9a9a9a;
}
*{margin:0;padding:0;box-sizing:border-box}
html,body{width:1200px;height:1011px;overflow:hidden;background:var(--paper)}
body{position:relative;font-family:'Ubuntu',sans-serif}
.card,.letterhead{position:absolute;overflow:hidden}
.card--dark{background:var(--ink-black);color:#fff}
.card--light{background:var(--paper);border:1px solid var(--edge);color:var(--navy)}
.letterhead{background:var(--paper);border:1px solid #b5b5b5;color:#222}
.landscape{width:206px;height:134px}
.portrait{width:134px;height:206px}

.wordmark{position:absolute;font-weight:500;font-size:10px;line-height:1.25;letter-spacing:.08em;text-transform:uppercase;white-space:nowrap}
.card--dark .wordmark{color:#fff}
.card--light .wordmark,.letterhead .wordmark{color:var(--navy)}
.portrait .wordmark{font-size:8px;letter-spacing:.06em}

.holder{position:absolute;font-size:11px;font-weight:500;letter-spacing:.02em}
.card--dark .holder{color:var(--sky)}
.contacts{position:absolute;font-size:6.8px;line-height:8.6px;font-weight:500;list-style:none}
.contacts li{display:flex}
.contacts .key{width:15px}
.card--dark .contacts .key{color:var(--sky)}
.card--light .contacts .key{color:var(--maroon)}
.tagline{position:absolute;font-size:7px;font-weight:500;white-space:nowrap}
.card--dark .tagline{color:var(--sky)}
.card--light .tagline{color:var(--maroon)}
.tagline--vertical{writing-mode:vertical-rl;transform:rotate(180deg);font-size:5.6px;font-weight:400}
.portrait .holder{font-size:8.5px}
.portrait .contacts{font-size:5.6px;line-height:7px}
.portrait .contacts .key{width:12px}
.portrait .tagline{font-size:5.2px}

.head-contacts{position:absolute;font-size:3.4px;line-height:4.3px;list-style:none;white-space:nowrap}
.head-contacts .key{color:var(--maroon)}
.head-contacts--right{text-align:right}
.letterhead .wordmark{font-size:11px}
.wordmark--vertical{writing-mode:vertical-rl;transform:rotate(180deg);font-size:8px!important}
.rule{position:absolute;width:.8px;background:var(--navy)}
.footer{position:absolute;left:0;right:0;top:320px;text-align:center;font-size:3.3px;line-height:4.2px;color:#222}
.footer span{margin:0 5px}
.sign-off{position:absolute;left:12px;top:281px;font-size:4.2px;line-height:5.2px}
.sign-off .name{color:var(--navy);font-weight:500;font-size:5px;margin-bottom:3px}
.sign-off ul{list-style:none}
.sign-off .key{color:var(--maroon);display:inline-block;width:8px}
</style>
</head>
<body>

<!-- Row 1: landscape cards, details left -->
<div class="card card--dark landscape" style="left:81px;top:48px">
  <div class="wordmark" style="left:86px;top:44px">Bramwell<br>Property Finders</div>
</div>
<div class="card card--dark landscape" style="left:330px;top:48px">
  <div class="holder" style="left:13px;top:70px">Owen Bramwell</div>
  <ul class="contacts" style="left:13px;top:88px">
    <li><span class="key">t:</span>0208 394 2261</li>
    <li><span class="key">m:</span>+44(0)7940 318 472</li>
    <li><span class="key">e:</span>info@bramwellpropertyfinders.co.uk</li>
    <li><span class="key">w:</span>bramwellpropertyfinders.co.uk</li>
  </ul>
  <div class="tagline tagline--vertical" style="left:194px;top:7px">London Property Finders and Search Agents</div>
</div>
<div class="card card--light landscape" style="left:663px;top:48px">
  <div class="wordmark" style="left:86px;top:44px">Bramwell<br>Property Finders</div>
</div>
<div class="card card--light landscape" style="left:912px;top:48px">
  <div class="holder" style="left:13px;top:70px">Owen Bramwell</div>
  <ul class="contacts" style="left:13px;top:88px">
    <li><span class="key">t:</span>0208 394 2261</li>
    <li><span class="key">m:</span>+44(0)7940 318 472</li>
    <li><span class="key">e:</span>info@bramwellpropertyfinders.co.uk</li>
    <li><span class="key">w:</span>bramwellpropertyfinders.co.uk</li>
  </ul>
  <div class="tagline tagline--vertical" style="left:194px;top:7px">London Property Finders and Search Agents</div>
</div>

<!-- Row 2: landscape cards, name top right -->
<div class="card card--dark landscape" style="left:81px;top:202px">
  <div class="wordmark" style="left:21px;top:92px">Bramwell<br>Property Finders</div>
</div>
<div class="card card--dark landscape" style="left:330px;top:202px">
  <div class="holder" style="right:15px;top:12px;font-size:12.5px">Owen Bramwell</div>
  <ul class="contacts" style="left:13px;top:70px">
    <li><span class="key">t:</span>0208 394 2261</li>
    <li><span class="key">m:</span>+44(0)7940 318 472</li>
    <li><span class="key">e:</span>info@bramwellpropertyfinders.co.uk</li>
    <li><span class="key">w:</span>bramwellpropertyfinders.co.uk</li>
  </ul>
  <div class="tagline" style="left:13px;top:115px">London Property Finders and Search Agents</div>
</div>
<div class="card card--light landscape" style="left:663px;top:202px">
  <div class="wordmark" style="left:21px;top:92px">Bramwell<br>Property Finders</div>
</div>
<div class="card card--light landscape" style="left:912px;top:202px">
  <div class="holder" style="right:15px;top:12px;font-size:12.5px">Owen Bramwell</div>
  <ul class="contacts" style="left:13px;top:70px">
    <li><span class="key">t:</span>0208 394 2261</li>
    <li><span class="key">m:</span>+44(0)7940 318 472</li>
    <li><span class="key">e:</span>info@bramwellpropertyfinders.co.uk</li>
    <li><span class="key">w:</span>bramwellpropertyfinders.co.uk</li>
  </ul>
  <div class="tagline" style="left:13px;top:115px">London Property Finders and Search Agents</div>
</div>

<!-- Row 3: portrait cards -->
<div class="card card--dark portrait" style="left:117px;top:360px">
  <div class="wordmark" style="left:22px;top:56px">Bramwell<br>Property Finders</div>
</div>
<div class="card card--dark portrait" style="left:366px;top:360px">
  <div class="holder" style="left:8px;top:138px">Owen Bramwell</div>
  <ul class="contacts" style="left:8px;top:154px">
    <li><span class="key">t:</span>0208 394 2261</li>
    <li><span class="key">m:</span>+44(0)7940 318 472</li>
    <li><span class="key">e:</span>info@bramwellpropertyfinders.co.uk</li>
    <li><span class="key">w:</span>bramwellpropertyfinders.co.uk</li>
  </ul>
  <div class="tagline" style="left:8px;top:194px">London Property Finders and Search Agents</div>
</div>
<div class="card card--light portrait" style="left:700px;top:360px">
  <div class="wordmark" style="left:22px;top:56px">Bramwell<br>Property Finders</div>
</div>
<div class="card card--light portrait" style="left:949px;top:360px">
  <div class="holder" style="left:8px;top:138px">Owen Bramwell</div>
  <ul class="contacts" style="left:8px;top:154px">
    <li><span class="key">t:</span>0208 394 2261</li>
    <li><span class="key">m:</span>+44(0)7940 318 472</li>
    <li><span class="key">e:</span>info@bramwellpropertyfinders.co.uk</li>
    <li><span class="key">w:</span>bramwellpropertyfinders.co.uk</li>
  </ul>
  <div class="tagline" style="left:8px;top:194px">London Property Finders and Search Agents</div>
</div>

<!-- Letterheads -->
<div class="letterhead" style="left:43px;top:619px;width:243px;height:343px">
  <div class="wordmark wordmark--vertical" style="left:9px;top:11px">Bramwell<br>Property Finders</div>
  <ul class="head-contacts head-contacts--right" style="right:10px;top:11px">
    <li><span class="key">t:</span> 0208 394 2261</li>
    <li><span class="key">m:</span> +44(0)7940 318 472</li>
    <li><span class="key">e:</span> info@bramwellpropertyfinders.co.uk</li>
    <li><span class="key">w:</span> bramwellpropertyfinders.co.uk</li>
  </ul>
  <div class="footer">Pemberly Holdings Ltd Trading as Bramwell Property Finders, a company registered in England &amp; Wales, No.5917302<br>Registered office is 41 Kelmscott House, Ashdown Lane, London, SW9 7QJ<br><span>t: 0208 394 2261</span><span>m: +44(0)7940 318 472</span><span>e: info@bramwellpropertyfinders.co.uk</span></div>
</div>

<div class="letterhead" style="left:333px;top:619px;width:243px;height:343px">
  <div class="wordmark" style="right:76px;top:7px;text-align:right">Bramwell<br>Property Finders</div>
  <div class="rule" style="left:172px;top:0;height:37px"></div>
  <ul class="head-contacts" style="left:175px;top:14px">
    <li><span class="key">t:</span> 0208 394 2261</li>
    <li><span class="key">m:</span> +44(0)7940 318 472</li>
    <li><span class="key">e:</span> info@bramwellpropertyfinders.co.uk</li>
    <li><span class="key">w:</span> bramwellpropertyfinders.co.uk</li>
  </ul>
  <div class="footer">Pemberly Holdings Ltd Trading as Bramwell Property Finders, a company registered in England &amp; Wales, No.5917302<br>Registered office is 41 Kelmscott House, Ashdown Lane, London, SW9 7QJ<br><span>t: 0208 394 2261</span><span>m: +44(0)7940 318 472</span><span>e: info@bramwellpropertyfinders.co.uk</span></div>
</div>

<div class="letterhead" style="left:623px;top:619px;width:243px;height:343px">
  <div class="wordmark" style="left:13px;top:12px">Bramwell<br>Property Finders</div>
  <ul class="head-contacts head-contacts--right" style="right:13px;top:13px">
    <li><span class="key">t:</span> 0208 394 2261</li>
    <li><span class="key">m:</span> +44(0)7940 318 472</li>
    <li><span class="key">e:</span> info@bramwellpropertyfinders.co.uk</li>
    <li><span class="key">w:</span> bramwellpropertyfinders.co.uk</li>
  </ul>
  <div class="footer">Pemberly Holdings Ltd Trading as Bramwell Property Finders, a company registered in England &amp; Wales, No.5917302<br>Registered office is 41 Kelmscott House, Ashdown Lane, London, SW9 7QJ<br><span>t: 0208 394 2261</span><span>m: +44(0)7940 318 472</span><span>e: info@bramwellpropertyfinders.co.uk</span></div>
</div>

<div class="letterhead" style="left:913px;top:619px;width:243px;height:343px">
  <div class="wordmark" style="right:16px;top:12px;text-align:right">Bramwell<br>Property Finders</div>
  <div class="sign-off">
    <div class="name">Bramwell Property Finders</div>
    <ul>
      <li><span class="key">t:</span>0208 394 2261</li>
      <li><span class="key">m:</span>+44(0)7940 318 472</li>
      <li><span class="key">e:</span>info@bramwellpropertyfinders.co.uk</li>
      <li><span class="key">w:</span>bramwellpropertyfinders.co.uk</li>
    </ul>
  </div>
  <div class="footer">Pemberly Holdings Ltd Trading as Bramwell Property Finders, a company registered in England &amp; Wales, No.5917302<br>Registered office is 41 Kelmscott House, Ashdown Lane, London, SW9 7QJ<br><span>t: 0208 394 2261</span><span>m: +44(0)7940 318 472</span><span>e: info@bramwellpropertyfinders.co.uk</span></div>
</div>

</body>
</html>
```